Park Company Mobile Application Design

We are looking for deisgn of the mobile application for the parking company. More details about the parking company you can find on the following web site: www.tvr.mk.
As well we attached the parking card that this company is issuing. As you may see their preferred color is green.
Attached you can find screens that we are planning to implement in the mobile application.
If you need more details please contact us on goran@brelo.mk.

Thanks,
Goran Dimovski
Brelo Group

```html
<!DOCTYPE html>
<html lang="en">
<head>
<meta charset="utf-8">
<title>CityPark – Mobile App Screens</title>
<link href="https://fonts.googleapis.com/css2?family=Poppins:wght@400;500;600;700;800&family=Inter:wght@500&display=swap" rel="stylesheet">
<style>
  :root {
    --sky-top: #10d6ff;
    --sky-bottom: #05c3f7;
    --slate: #363f52;
    --slate-field: #5a6170;
    --green: #13b447;
    --green-bright: #14c244;
    --white: #ffffff;
    --field-light: #f3f3f3;
    --field-border: #e4e4e4;
    --ink: #2b2f38;
    --muted: #8d929b;
    --map: #e8eaed;
    --pin-dark: #2e3340;
  }
  * { box-sizing: border-box; margin: 0; padding: 0; }
  html, body { width: 909px; height: 1200px; overflow: hidden; }
  body {
    position: relative;
    background: linear-gradient(180deg, var(--sky-top), var(--sky-bottom));
    font-family: "Poppins", sans-serif;
    color: var(--ink);
  }
  .screen-title {
    position: absolute; width: 260px; text-align: center;
    font-weight: 700; font-size: 24px; color: var(--white); line-height: 1;
  }
  .phone {
    position: absolute; width: 222px; height: 406px; border-radius: 16px;
    overflow: hidden; background: var(--white);
  }
  .phone.dark { background: var(--slate); }
  .status-bar {
    position: absolute; top: 0; left: 0; right: 0; height: 14px;
    font-family: "Inter", sans-serif; font-size: 8px; font-weight: 500;
    display: flex; align-items: center; justify-content: space-between; padding: 0 10px;
    color: var(--white); z-index: 3;
  }
  .status-bar.on-light { color: #111; }
  .status-bar .time { position: absolute; left: 0; right: 0; text-align: center; }
  .status-bar .battery { display: flex; align-items: center; gap: 3px; }
  .status-bar .battery i {
    display: inline-block; width: 15px; height: 7px; border: 1px solid currentColor; border-radius: 2px;
    background: currentColor; box-shadow: inset 0 0 0 1px var(--slate);
  }
  .status-bar.on-light .battery i { box-shadow: none; background: #111; }
  .dark-head { position: absolute; left: 0; right: 0; top: 0; background: var(--slate); }
  .dark-head::after {
    content: ""; position: absolute; bottom: -1px; left: 50%; margin-left: -5px;
    border: 5px solid transparent; border-bottom-color: var(--white);
  }
  .brand {
    position: absolute; left: 0; right: 0; display: flex; align-items: center; justify-content: center; gap: 6px;
    font-weight: 700; font-size: 22px; color: var(--green-bright); line-height: 1;
  }
  .brand .dot { width: 14px; height: 14px; border-radius: 50%; background: var(--green-bright); }
  .field {
    position: absolute; left: 29px; width: 163px; height: 26px; border-radius: 3px;
    background: var(--slate-field); color: #d5d8de; font-size: 9.5px;
    display: flex; align-items: center; padding-left: 14px;
  }
  .field.light {
    left: 15px; width: 193px; background: var(--field-light); border: 1px solid var(--field-border);
    color: var(--muted); font-size: 9px; padding-left: 15px;
  }
  .field.outline {
    left: 14px; width: 193px; background: var(--white); border: 1px solid #d9dbe0; border-radius: 4px;
    color: var(--muted); font-size: 7.5px; padding-left: 11px; gap: 9px;
  }
  .field.outline svg { width: 10px; height: 10px; stroke: #a4a8b0; fill: none; stroke-width: 1.2; }
  .password-dots { letter-spacing: 2px; font-size: 13px; color: var(--white); }
  .btn {
    position: absolute; left: 29px; width: 163px; height: 26px; border-radius: 3px;
    display: flex; align-items: center; justify-content: center; font-size: 11px; color: var(--white);
  }
  .btn.primary { background: var(--green); }
  .btn.secondary { background: var(--slate-field); }
  .btn.wide { left: 15px; width: 193px; height: 27px; border-radius: 4px; background: var(--green-bright); font-size: 11.5px; }
  .btn.ghost { background: var(--white); border: 1px solid var(--green-bright); color: var(--ink); }
  .caption { position: absolute; left: 0; right: 0; text-align: center; font-size: 7px; font-weight: 500; color: var(--white); }
  .or-divider { position: absolute; left: 29px; width: 163px; display: flex; align-items: center; gap: 4px; font-size: 6.5px; color: #aab0bb; }
  .or-divider::before, .or-divider::after { content: ""; flex: 1; height: 1px; background: #5e6576; }
  .panel-heading { position: absolute; left: 0; right: 0; text-align: center; font-size: 11px; font-weight: 500; color: var(--ink); }
  .radio { position: absolute; left: 19px; display: flex; align-items: center; gap: 10px; font-size: 7px; color: var(--muted); }
  .radio i { width: 8px; height: 8px; border-radius: 50%; background: #eee; display: inline-block; position: relative; }
  .radio.checked i::after { content: ""; position: absolute; inset: 2px; border-radius: 50%; background: #777; }
  .top-nav { position: absolute; top: 20px; left: 14px; right: 14px; display: flex; justify-content: space-between; align-items: center; }
  .menu-icon { width: 17px; height: 12px; display: flex; flex-direction: column; justify-content: space-between; }
  .menu-icon span { height: 1.5px; background: var(--green-bright); }
  .map-link { display: flex; align-items: center; gap: 3px; color: var(--green-bright); font-size: 11px; }
  .tab-bar {
    position: absolute; left: 0; right: 0; bottom: 0; height: 31px; border-top: 1px solid #e6e7ea; background: var(--white);
    display: flex; justify-content: space-between; align-items: center; padding: 0 20px;
  }
  .tab-bar svg { width: 15px; height: 13px; fill: none; stroke: #b8bcc3; stroke-width: 1.2; }
  .tab-bar .active svg { stroke: var(--green-bright); fill: var(--green-bright); }
  .map-area { position: absolute; inset: 0 0 31px 0; background: linear-gradient(160deg, #eceef1, #e3e6ea); }
  .back-arrow { position: absolute; left: 15px; top: 24px; width: 13px; height: 11px; stroke: #555; fill: none; stroke-width: 1.4; }
  .search-bar {
    position: absolute; left: 15px; top: 55px; width: 193px; height: 29px; border-radius: 4px; background: var(--white);
    box-shadow: 0 2px 6px rgba(0,0,0,.08); display: flex; align-items: center; gap: 14px; padding-left: 9px;
    font-size: 9px; color: #b6bac1;
  }
  .search-bar svg { width: 15px; height: 15px; stroke: #b6bac1; fill: none; stroke-width: 1.2; }
  .price-pin {
    position: absolute; height: 17px; border-radius: 9px; display: flex; align-items: center; gap: 6px; padding-left: 2px;
    background: var(--white); color: var(--ink); font-size: 7.5px; box-shadow: 0 1px 3px rgba(0,0,0,.1);
  }
  .price-pin.selected { background: var(--pin-dark); color: var(--white); }
  .price-pin b {
    width: 12px; height: 12px; border-radius: 50%; background: var(--pin-dark); color: var(--white);
    font-size: 7px; display: flex; align-items: center; justify-content: center;
  }
  .price-pin.selected b { background: var(--white); color: var(--pin-dark); }
  .price-pin::after { content: ""; position: absolute; left: 50%; top: 17px; width: 1px; height: 6px; background: var(--pin-dark); }
  .you-here { position: absolute; left: 78px; top: 290px; font-size: 5px; color: #555; background: var(--white); padding: 1px 4px; border-radius: 5px; }
  .location-dot { position: absolute; left: 90px; top: 304px; width: 11px; height: 11px; border-radius: 50%; background: #4a90e2; box-shadow: 0 0 0 3px rgba(74,144,226,.3); }
  .footer-note { position: absolute; left: 0; right: 0; top: 1075px; text-align: center; font-weight: 700; font-size: 32px; color: var(--white); }
</style>
</head>
<body>

  <!-- Row 1 -->
  <h2 class="screen-title" style="left:70px;top:48px">Home Page</h2>
  <h2 class="screen-title" style="left:324px;top:48px">Login Page</h2>
  <h2 class="screen-title" style="left:602px;top:48px">Register</h2>

  <section class="phone dark" style="left:89px;top:91px" aria-label="Home screen">
    <div class="status-bar"><span>●●●○○</span><span class="time">4:21 PM</span><span class="battery">100% <i></i></span></div>
    <div class="brand" style="top:120px"><span class="dot"></span>CityPark</div>
    <div class="btn primary" style="top:277px">Login</div>
    <div class="btn secondary" style="top:316px">Register</div>
  </section>

  <section class="phone dark" style="left:355px;top:91px" aria-label="Login screen">
    <div class="status-bar"><span>●●●○○</span><span class="time">4:21 PM</span><span class="battery">100% <i></i></span></div>
    <div class="brand" style="top:78px"><span class="dot"></span>CityPark</div>
    <div class="field" style="top:146px">user123@mailbox.com</div>
    <div class="field password-dots" style="top:188px">●●●●●</div>
    <div class="btn primary" style="top:228px">Login</div>
    <div class="caption" style="top:268px">Forgot Password?</div>
    <div class="or-divider" style="top:290px">OR</div>
    <div class="caption" style="top:310px">New to Park?</div>
    <div class="btn secondary" style="top:332px">Register</div>
  </section>

  <section class="phone" style="left:621px;top:91px" aria-label="Register screen">
    <div class="dark-head" style="height:146px"></div>
    <div class="status-bar"><span>●●●○○</span><span class="time">4:21 PM</span><span class="battery">100% <i></i></span></div>
    <div class="brand" style="top:62px"><span class="dot"></span>CityPark</div>
    <div class="panel-heading" style="top:154px">Register Now</div>
    <div class="field light" style="top:193px">Enter Email ID</div>
    <div class="field light" style="top:229px">Enter Password</div>
    <div class="field light" style="top:265px">Confirm Password</div>
    <div class="field light" style="top:301px">Enter Phone</div>
    <div class="btn wide" style="top:351px">Register</div>
  </section>

  <!-- Row 2 -->
  <h2 class="screen-title" style="left:70px;top:558px">Forgot Password</h2>
  <h2 class="screen-title" style="left:336px;top:560px">Pay Parking</h2>
  <h2 class="screen-title" style="left:604px;top:560px">Map Page</h2>

  <section class="phone" style="left:89px;top:599px" aria-label="Forgot password screen">
    <div class="dark-head" style="height:148px"></div>
    <div class="status-bar"><span>●●●○○</span><span class="time">4:21 PM</span><span class="battery">100% <i></i></span></div>
    <div class="brand" style="top:63px"><span class="dot"></span>CityPark</div>
    <div class="panel-heading" style="top:154px">Forgot Password?</div>
    <div class="field light" style="top:193px">Registerd Email ID</div>
    <div class="radio checked" style="top:238px"><i></i>Send Via Email</div>
    <div class="radio" style="top:256px"><i></i>Send Via SMS</div>
    <div class="btn wide" style="top:292px">Send Code</div>
    <div class="btn wide ghost" style="top:336px">Reset Password</div>
  </section>

  <section class="phone" style="left:355px;top:599px" aria-label="Pay parking screen">
    <div class="status-bar on-light"><span>●●●○○</span><span class="time">4:21 PM</span><span class="battery">100% <i></i></span></div>
    <nav class="top-nav">
      <div class="menu-icon"><span></span><span></span><span></span></div>
      <div class="map-link"><svg width="7" height="9" viewBox="0 0 7 9"><path d="M3.5 0A3.3 3.3 0 0 0 .2 3.3C.2 5.8 3.5 9 3.5 9s3.3-3.2 3.3-5.7A3.3 3.3 0 0 0 3.5 0zm0 4.6a1.3 1.3 0 1 1 0-2.6 1.3 1.3 0 0 1 0 2.6z" fill="var(--green-bright)"/></svg>Map</div>
    </nav>
    <div class="panel-heading" style="top:57px;font-weight:600">Pay Parking</div>
    <div class="field outline" style="top:97px"><svg viewBox="0 0 10 10"><path d="M5 .6a3 3 0 0 0-3 3c0 2.3 3 5.8 3 5.8s3-3.5 3-5.8a3 3 0 0 0-3-3z"/><circle cx="5" cy="3.6" r="1"/></svg>Parking Zone</div>
    <div class="field outline" style="top:136px"><svg viewBox="0 0 10 10"><circle cx="5" cy="5" r="4.3"/><path d="M5 2.5V5h2"/></svg>Parking Duration</div>
    <div class="field outline" style="top:176px"><svg viewBox="0 0 10 10"><path d="M1 7V5l1.5-3h5L9 5v2zM1 7v1.5h1.5V7M7.5 7v1.5H9V7M1 5h8"/></svg>License&nbsp; Number</div>
    <div class="btn wide" style="left:14px;top:236px">Pay Now</div>
    <nav class="tab-bar">
      <span class="active"><svg viewBox="0 0 15 13"><path d="M1 11V7l2-4h9l2 4v4z"/></svg></span>
      <span><svg viewBox="0 0 15 13"><rect x="1" y="2" width="13" height="10" rx="1"/><path d="M3 9h4M9 5h3M9 8h3"/></svg></span>
      <span><svg viewBox="0 0 15 13"><circle cx="7.5" cy="6.5" r="5.7"/><path d="M7.5 3.5v3.5M7.5 8.8v.6"/></svg></span>
    </nav>
  </section>

  <section class="phone" style="left:623px;top:599px" aria-label="Map screen">
    <div class="map-area" role="img" aria-label="City street map around the user's location with nearby parking areas"></div>
    <div class="status-bar on-light"><span>●●●○○</span><span class="time">4:21 PM</span><span class="battery">100% <i></i></span></div>
    <svg class="back-arrow" viewBox="0 0 13 11"><path d="M12.5 5.5H1M5.5 1 1 5.5 5.5 10"/></svg>
    <div class="search-bar"><svg viewBox="0 0 15 15"><circle cx="6.5" cy="6.5" r="5.5"/><path d="M10.5 10.5 14 14"/></svg>Search Location</div>
    <div class="price-pin selected" style="left:38px;top:120px;width:65px"><b>P</b>1000/h</div>
    <div class="price-pin" style="left:128px;top:161px;width:51px"><b>P</b>2000/h</div>
    <div class="price-pin" style="left:2px;top:212px;width:63px"><b>P</b>7000/h</div>
    <div class="price-pin" style="left:131px;top:257px;width:65px"><b>P</b>5000/h</div>
    <div class="you-here">You're Here</div>
    <div class="location-dot"></div>
    <nav class="tab-bar">
      <span><svg viewBox="0 0 15 13"><path d="M1 11V7l2-4h9l2 4v4z"/></svg></span>
      <span><svg viewBox="0 0 15 13"><rect x="1" y="2" width="13" height="10" rx="1"/><path d="M3 9h4M9 5h3M9 8h3"/></svg></span>
      <span><svg viewBox="0 0 15 13"><circle cx="7.5" cy="6.5" r="5.7"/><path d="M7.5 3.5v3.5M7.5 8.8v.6"/></svg></span>
    </nav>
  </section>

  <p class="footer-note">More Pages Will submitted soon Please wait</p>

</body>
</html>
```